Business Card Design Project

Hi,
I am after a business card design for a new business. The business is called Hollow Crest and is a stockist of building supplies used for modern cosmetic renovations for houses. (e.g Floorboards, timber decking, modern fittings and fixtures.)
The logo and font faces have been attached.
The logo comes in 2 different color scheme's - 1. Orange on White & 2. Orange on Black. I would like 2 versions of the business card design to reflect these color scheme's.
The designs need to be double sided. The front should contain all the contact information, whilst the back of the card should display the logo and the URL of the webpage - www.hollowcrest-example.com.au . The logo needs to be displayed creatively on the back of the card.
The business card design needs to reflect the image of modern living, but should also have the wow factor.

```html
<!DOCTYPE html>
<html lang="en">
<head>
<meta charset="utf-8">
<title>Hollow Crest – Business Card Options</title>
<link rel="stylesheet" href="https://fonts.googleapis.com/css2?family=Roboto+Condensed:wght@300;400&family=Arimo:ital,wght@0,400;1,400&display=swap">
<style>
  :root {
    --page: #ffffff;
    --ink: #111111;
    --black: #000000;
    --brown: #331a10;
    --rust: #a5452a;
    --orange: #f26b21;
    --orange-deep: #c9501a;
    --shadow-brown: #5a210c;
    --white: #ffffff;
    --sans: "Arimo", Arial, sans-serif;
    --display: "Roboto Condensed", "Arial Narrow", sans-serif;
  }
  * { box-sizing: border-box; margin: 0; padding: 0; }
  html, body { width: 1200px; height: 900px; overflow: hidden; background: var(--page); }
  .sheet { position: relative; width: 1200px; height: 900px; font-family: var(--sans); color: var(--ink); }

  .option-label { position: absolute; left: 20px; font-size: 19px; }
  .side-label { position: absolute; width: 200px; text-align: center; font-size: 18px; text-decoration: underline; }

  .card { position: absolute; width: 561px; height: 301px; overflow: hidden; }
  .card svg.backdrop { position: absolute; inset: 0; width: 100%; height: 100%; }
  .card--black { background: var(--black); }
  .card--brown { background: var(--brown); }

  .wordmark {
    position: absolute; font-family: var(--display); font-weight: 300;
    color: var(--orange); line-height: 0.95; font-size: 50px;
  }
  .brand-lockup { position: absolute; display: flex; align-items: center; gap: 20px; }
  .brand-lockup .mark-square { width: 82px; height: 82px; background: var(--orange); }
  .brand-lockup .wordmark { position: static; }
  .legal-suffix {
    position: absolute; color: var(--white); font-size: 20px; font-family: var(--sans);
    transform: rotate(-90deg); transform-origin: left top;
  }

  .contact { position: absolute; color: var(--white); font-size: 9px; font-style: italic; line-height: 13px; }
  .contact dt { display: inline-block; width: 36px; }
  .contact dd { display: inline; }
  .contact dd::after { content: ""; display: block; }

  .trade-line { position: absolute; font-size: 8px; color: var(--white); }
  .trade-line .lead { color: var(--orange); }
  .site-url { position: absolute; font-size: 9px; font-style: italic; }
</style>
</head>
<body>
<main class="sheet">

  <!-- Option 1 -->
  <p class="option-label" style="top:32px">Option-1</p>

  <section class="card card--black" style="left:12px; top:62px" aria-label="Option 1 front">
    <svg class="backdrop" viewBox="0 0 561 301" aria-hidden="true">
      <defs>
        <linearGradient id="sweep" x1="0" y1="0" x2="1" y2="1">
          <stop offset="0" stop-color="#f47a2c"/>
          <stop offset="1" stop-color="#d2541b"/>
        </linearGradient>
      </defs>
      <path d="M0 0 H118 L228 238 Q240 275 208 301 H0 Z" fill="var(--shadow-brown)"/>
      <path d="M0 0 H108 L216 232 Q228 268 192 301 H0 Z" fill="url(#sweep)"/>
    </svg>
    <dl class="contact" style="left:12px; top:163px">
      <dt>Phone</dt><dd>(+61) 000-55012-000</dd>
      <dt>Mobile</dt><dd>(+61) 000-55012-000</dd>
      <dd>hollowcrest-example.com.au</dd>
    </dl>
    <h2 class="wordmark" style="left:276px; top:76px">Hollow<br>Crest</h2>
    <p class="trade-line" style="left:301px; top:287px"><span class="lead">We deals in :</span> &nbsp;Floorboards, timber decking, modern fittings and fixtures</p>
  </section>

  <section class="card card--black" style="left:627px; top:62px" aria-label="Option 1 back">
    <p class="site-url" style="right:10px; top:6px; color:var(--orange)">www.hollowcrest-example.com.au</p>
    <div class="brand-lockup" style="left:85px; top:104px">
      <span class="mark-square"></span>
      <h2 class="wordmark">Hollow<br>Crest</h2>
    </div>
    <p class="legal-suffix" style="left:444px; top:183px">pty ltd</p>
  </section>

  <p class="side-label" style="left:132px; top:370px">Front</p>
  <p class="side-label" style="left:789px; top:370px">Back</p>

  <!-- Option 2 -->
  <p class="option-label" style="top:472px">Option-2</p>

  <section class="card card--brown" style="left:12px; top:503px; height:303px" aria-label="Option 2 front">
    <svg class="backdrop" viewBox="0 0 561 303" aria-hidden="true">
      <polygon points="56,0 66,0 0,62 0,52" fill="var(--orange)"/>
      <polygon points="80,0 104,0 0,106 0,82" fill="var(--orange)"/>
      <rect x="398" y="0" width="163" height="303" fill="var(--rust)"/>
      <rect x="398" y="0" width="2" height="303" fill="var(--orange-deep)"/>
    </svg>
    <h2 class="wordmark" style="left:78px; top:96px; font-size:54px">Hollow<br>Crest</h2>
    <dl class="contact" style="left:414px; top:111px">
      <dt>Phone</dt><dd>(+61) 000-55012-000</dd>
      <dt>Mobile</dt><dd>(+61) 000-55012-000</dd>
      <dd>hello@hollowcrest-example.com.au</dd>
    </dl>
    <p class="trade-line" style="left:9px; top:290px">We deals in : Floorboards, timber decking, modern fittings and fixtures</p>
  </section>

  <section class="card card--brown" style="left:622px; top:503px; width:565px; height:303px" aria-label="Option 2 back">
    <svg class="backdrop" viewBox="0 0 565 303" aria-hidden="true">
      <polygon points="565,186 565,212 472,303 444,303" fill="var(--orange)"/>
      <polygon points="565,230 565,242 502,303 490,303" fill="var(--orange)"/>
    </svg>
    <p class="site-url" style="left:10px; top:9px; color:var(--white); font-style:normal; font-size:8px">www.hollowcrest-example.com.au</p>
    <div class="brand-lockup" style="left:86px; top:104px">
      <span class="mark-square"></span>
      <h2 class="wordmark">Hollow<br>Crest</h2>
    </div>
    <p class="legal-suffix" style="left:452px; top:192px">pty ltd</p>
  </section>

  <p class="side-label" style="left:132px; top:815px">Front</p>
  <p class="side-label" style="left:789px; top:815px">Back</p>

</main>
</body>
</html>
```